Relay Party needs Credential Design

The Dale Prentiss Foundation needs a credential designed for guests. The event will take place on Relay Tuesday in Boston. We are looking for something to send to guests before the event with event information and to designate them as a guest of the Foundation. We would like it be a vertical design that can be attached to a lanyard.

Industry/Entity Type

Non Profit

Font styles to use
Serif
Sans Serif

Requirements
Must have
• The information should include the date, Dale Prentiss Foundation Logo, and "Harborline Relay Celebration"
Nice to have
• Harborline Relay Logo

```html
<!DOCTYPE html>
<html lang="en">
<head>
<meta charset="utf-8">
<title>Dale Prentiss Foundation – Harborline Relay Celebration Credential</title>
<link rel="stylesheet" href="https://fonts.googleapis.com/css2?family=Yanone+Kaffeesatz:wght@500;700&family=Fira+Sans:wght@700;800&family=Tinos:ital@0;1&display=swap">
<style>
  :root {
    --frame-grey: #6b6f71;
    --title-grey: #6a6e70;
    --foundation-green: #12904a;
    --paper: #ffffff;
    --mic-light: #e9eaeb;
    --mic-mid: #c9cbcd;
    --sponsor-blue: #5db6df;
  }
  html, body {
    margin: 0;
    padding: 0;
    width: 930px;
    height: 1200px;
    overflow: hidden;
    background: var(--paper);
  }
  .credential {
    position: relative;
    width: 930px;
    height: 1200px;
  }
  .credential svg { display: block; }
  .title-small { font-family: "Yanone Kaffeesatz", "Arial Narrow", sans-serif; font-weight: 700; fill: var(--title-grey); }
  .title-name { font-family: "Yanone Kaffeesatz", "Arial Narrow", sans-serif; font-weight: 700; fill: var(--foundation-green); }
  .title-foundation { font-family: "Yanone Kaffeesatz", "Arial Narrow", sans-serif; font-weight: 500; fill: var(--title-grey); }
  .event-year { font-family: "Fira Sans", Arial, sans-serif; font-weight: 800; fill: var(--foundation-green); }
  .event-name { font-family: "Fira Sans", Arial, sans-serif; font-weight: 700; fill: var(--title-grey); }
  .event-details { font-family: "Tinos", "Times New Roman", serif; fill: var(--paper); font-size: 31px; }
  .sponsor-label { font-family: "Tinos", "Times New Roman", serif; font-style: italic; fill: var(--paper); font-size: 15px; }
  .sponsor-name { font-family: "Tinos", "Times New Roman", serif; fill: var(--sponsor-blue); font-size: 27px; }
  .divider { stroke: var(--foundation-green); stroke-width: 2.5; stroke-dasharray: 2 5; }
</style>
</head>
<body>
<main class="credential">
  <svg width="930" height="1200" viewBox="0 0 930 1200" xmlns="http://www.w3.org/2000/svg">
    <defs>
      <linearGradient id="micTone" x1="0" y1="0" x2="0" y2="1">
        <stop offset="0" stop-color="var(--mic-mid)"/>
        <stop offset="0.45" stop-color="var(--mic-light)"/>
        <stop offset="1" stop-color="var(--paper)"/>
      </linearGradient>
      <radialGradient id="leafTone">
        <stop offset="0" stop-color="var(--foundation-green)" stop-opacity="0.55"/>
        <stop offset="1" stop-color="var(--foundation-green)" stop-opacity="0"/>
      </radialGradient>
      <clipPath id="innerArea"><rect x="29" y="29" width="872" height="1142"/></clipPath>
    </defs>

    <!-- frame -->
    <rect class="frame" x="0" y="0" width="930" height="1200" fill="var(--frame-grey)"/>
    <rect class="paper" x="29" y="29" width="872" height="1142" fill="var(--paper)"/>

    <g clip-path="url(#innerArea)">
      <!-- microphone artwork area -->
      <rect role="img" aria-label="Large faded vintage studio microphone with a smaller chrome microphone in front"
            x="505" y="70" width="380" height="1101" rx="150" fill="url(#micTone)"/>

      <!-- scattered butterfly decoration -->
      <rect role="img" aria-label="Scattered green butterflies along the right and bottom edges"
            x="480" y="560" width="421" height="611" fill="url(#leafTone)" opacity="0.6"/>

      <!-- event info circle -->
      <circle class="info-disc" cx="275" cy="1045" r="365" fill="var(--foundation-green)"/>
      <polygon class="info-arrow" fill="var(--paper)"
               points="144,690 208,690 208,758 246,758 176,826 106,758 144,758"/>

      <text class="event-details" x="70" y="870">The Dale Prentiss Foundation</text>
      <text class="event-details" x="70" y="911">Harborline Relay Celebration</text>
      <text class="event-details" x="70" y="952">Monday, April 18 2016</text>
      <text class="event-details" x="70" y="993">The Harbor Chophouse</text>
      <text class="event-details" x="70" y="1032">11AM-3PM</text>

      <text class="sponsor-label" x="32" y="1138">Sponsored by:</text>
      <circle cx="186" cy="1129" r="10" fill="var(--sponsor-blue)"/>
      <text class="sponsor-name" x="206" y="1138">Northgate Staffing</text>
    </g>

    <!-- title -->
    <text class="title-small" x="205" y="138" font-size="72">The</text>
    <text class="title-name" x="108" y="345" font-size="260" textLength="600" lengthAdjust="spacingAndGlyphs">Dale Prentiss</text>
    <text class="title-foundation" x="132" y="462" font-size="170" textLength="548" lengthAdjust="spacingAndGlyphs">FOUNDATION</text>

    <line class="divider" x1="29" y1="479" x2="901" y2="479"/>

    <!-- event name -->
    <text class="event-year" x="94" y="622" font-size="104">2016</text>
    <text class="event-name" x="344" y="569" font-size="44">Harborline</text>
    <text class="event-name" x="344" y="620" font-size="44">Relay</text>
    <text class="event-name" x="344" y="671" font-size="44">Celebration</text>
  </svg>
</main>
</body>
</html>
```